business card for law firm that reflects the web site -www.MarlaQuentby.com. That is pleasant to read

We need a business card for a small law firm. Your company designed our logo - tree of life - which I can provide to the designers. The card should be on both sides. Use the coloring from the web site (www.MarlaQuentby.com) and logo (I have several formats). I am attaching the logo, but not sure what format to use.

First side name of firm: Law Office of M.K. Quentby, P.A. 4819 West Pallisor, Suite 300, Phoenix, AZ 85016, Phone: 602.555.3841, Fax: 602.555.7290, web site: www.MarlaQuentby.com, email: MQuentby@MarlaQuentby.com.
Marla K. Quentby Bankruptcy and Foreclosure Attorney & Counselor.
Back side (perhaps vertical) the logo and then Notes with lines. At the bottom: Proud to help people and small businesses file for bankruptcy protection. We are a debt relief agency.
Updates

I have several versions of the logo. Will be happy to share whatever you need. Added Sunday, April 3, 2016

Target Market(s)

everyone

Industry/Entity Type

Legal

Contact Information for Business Card

I prefer something unique (rounded edges, design that adopts my web site - www.MarlaQuentby.com.

Font styles to use
Serif

Requirements
Must have
• First side name of firm: Law Office of M.K. Quentby, P.A. 4819 West Pallisor, Suite 300, Phoenix, AZ 85016, Phone: 602.555.3841, Fax: 602.555.7290, web site: www.MarlaQuentby.com, email: MQuentby@MarlaQuentby.com.
• Marla K. Quentby Bankruptcy and Foreclosure Attorney & Counselor.
• Back side (perhaps vertical) the logo and then Notes with lines. At the bottom: Proud to help people and small businesses file for bankruptcy protection. We are a debt relief agency.
• Green and brown colors that reflect the web site: www.MarlaQuentby.com
Should not have
• Type so small that older people cannot read.

```html
<!DOCTYPE html>
<html lang="en">
<head>
<meta charset="utf-8">
<title>Law Office of M.K. Quentby, P.A. — Business Card</title>
<link href="https://fonts.googleapis.com/css2?family=Libre+Baskerville:wght@400;700&family=Open+Sans:wght@400;600&display=swap" rel="stylesheet">
<style>
  :root {
    --bg: #e8e6e2;
    --card: #ffffff;
    --green: #1f6b34;
    --green-dark: #17502a;
    --brown: #6b3f1f;
    --ink: #2b2b2b;
    --rule: #3a3a3a;
    --line: #8a8a8a;
  }
  * { box-sizing: border-box; margin: 0; padding: 0; }
  html, body { width: 1200px; height: 800px; overflow: hidden; }
  body {
    background: var(--bg);
    font-family: "Open Sans", Arial, sans-serif;
    color: var(--ink);
    position: relative;
  }
  .card {
    position: absolute;
    background: var(--card);
    border-radius: 14px;
    box-shadow: 0 6px 18px rgba(0,0,0,0.18);
    overflow: hidden;
  }

  /* Back side (vertical) */
  .card-back { left: 110px; top: 130px; width: 340px; height: 560px; }
  .notes {
    position: absolute; left: 110px; top: 28px; width: 200px; height: 280px;
    display: flex; justify-content: space-between;
  }
  .notes span { width: 1px; height: 100%; background: var(--line); }
  .notes span:first-child { background: transparent; }
  .back-mark {
    position: absolute; left: 110px; top: 330px; width: 200px;
    display: flex; flex-direction: column; align-items: center; gap: 14px;
  }
  .back-mark .dot {
    width: 150px; height: 150px; border-radius: 50%;
    background: var(--brown);
    border: 14px solid var(--green);
  }
  .brand-name {
    font-family: "Libre Baskerville", Georgia, serif;
    font-weight: 700; color: var(--green); font-size: 20px;
    white-space: nowrap;
  }
  .mission {
    position: absolute; left: 34px; top: 28px; height: 504px;
    writing-mode: vertical-rl;
    font-size: 14px; line-height: 26px; color: var(--ink);
  }

  /* Front side */
  .card-front { left: 490px; top: 200px; width: 650px; height: 390px; }
  .front-mark {
    position: absolute; left: 0; top: 0; width: 220px; height: 330px;
    display: flex; flex-direction: column; align-items: center; justify-content: center; gap: 16px;
  }
  .front-mark .dot { width: 110px; height: 110px; border-radius: 50%; background: var(--green); }
  .front-info { position: absolute; left: 224px; top: 28px; right: 26px; }
  .firm {
    font-family: "Libre Baskerville", Georgia, serif; font-weight: 700;
    color: var(--green); text-transform: uppercase; line-height: 1.15;
    white-space: nowrap;
  }
  .firm .small { display: block; font-size: 21px; }
  .firm .large { display: block; font-size: 28px; }
  .rule { height: 2px; background: var(--rule); margin: 12px 0 14px; }
  .attorney {
    font-family: "Libre Baskerville", Georgia, serif; font-variant: small-caps;
    color: var(--green); font-size: 22px; text-align: right; white-space: nowrap;
  }
  .title { font-size: 13px; text-align: right; margin-top: 2px; white-space: nowrap; }
  .contacts { list-style: none; margin-top: 12px; }
  .contacts li {
    display: flex; justify-content: flex-end; align-items: center; gap: 8px;
    font-size: 15px; line-height: 25px; white-space: nowrap;
  }
  .icon { width: 16px; height: 16px; fill: var(--green-dark); flex: none; }
  .address {
    position: absolute; left: 30px; right: 26px; bottom: 20px;
    font-size: 14px; color: var(--green); text-transform: uppercase; letter-spacing: 0.5px;
    white-space: nowrap;
  }
</style>
</head>
<body>

<section class="card card-back" aria-label="Card back">
  <div class="notes" aria-label="Notes lines">
    <span></span><span></span><span></span><span></span><span></span><span></span><span></span><span></span>
  </div>
  <div class="back-mark">
    <div class="dot"></div>
    <div class="brand-name">M.K. Quentby</div>
  </div>
  <p class="mission">Proud to help people and small businesses file for bankruptcy protection<br>We are a debt relief agency</p>
</section>

<section class="card card-front" aria-label="Card front">
  <div class="front-mark">
    <div class="dot"></div>
    <div class="brand-name">M.K. Quentby</div>
  </div>
  <div class="front-info">
    <h1 class="firm"><span class="small">Law Office of</span><span class="large">M.K. Quentby, P.A</span></h1>
    <div class="rule"></div>
    <p class="attorney">Marla K. Quentby</p>
    <p class="title">Bankruptcy and Foreclosure Attorney &amp; Counselor</p>
    <ul class="contacts">
      <li>602.555.3841
        <svg class="icon" viewBox="0 0 16 16"><circle cx="8" cy="8" r="8"/><path d="M5 4h2l1 2-1 1c.5 1 1.5 2 2.5 2.5l1-1 2 1v2c-4 .5-8-3.5-7.5-7.5z" fill="#fff"/></svg></li>
      <li>602.555.7290
        <svg class="icon" viewBox="0 0 16 16"><circle cx="8" cy="8" r="8"/><rect x="4" y="6" width="8" height="5" fill="#fff"/><rect x="5.5" y="4" width="5" height="2" fill="#fff"/></svg></li>
      <li>www.MarlaQuentby.com
        <svg class="icon" viewBox="0 0 16 16"><circle cx="8" cy="8" r="8"/><circle cx="8" cy="8" r="4.5" fill="none" stroke="#fff"/><path d="M3.5 8h9M8 3.5v9" stroke="#fff"/></svg></li>
      <li>MQuentby@MarlaQuentby.com
        <svg class="icon" viewBox="0 0 16 16"><circle cx="8" cy="8" r="8"/><rect x="4" y="5" width="8" height="6" fill="#fff"/><path d="M4 5l4 3.5L12 5" fill="none" stroke="#17502a"/></svg></li>
    </ul>
  </div>
  <p class="address">4819 West Pallisor, Suite 300, Phoenix, AZ 85016</p>
</section>

</body>
</html>
```